The Harwell Selection Web Site design

I need a web design for my luxury range of Terry Toweling and Spa Accessories for luxury upmarket hotels and Spas. I have a catalog that sets the mood and tone I am looking for. I need a website design that shows off the look and feel of this luxury range while working back to the catalog look and feel. Its all about Upmarket and Luxury. I will be using the website as a reference site and as a site that customers can purchase off.
The Logo is attached as is the catalog. I don't mind changing the color of the Logo to match the website. However I would prefer to keep the font of that logo.

http://quillgallery.framevista.example/p559203417
Please can you try and access this link. The Harwell Selection
Name Trudie. Email trudie@kestrelsupply.example.au. Password Harwell.
These images are to be used for shopping page and please use the close up details of texture as background on pages and use those texture details and close ups for banners

Please note the look and feel has to be very upmarket and super luxury. Ficus is on mood and not on retail.
Have a look at the mood on the following websites
Www.velvetharbourstays.example
And oursandycovecottagestore.example
That one is retail .mi don't want retail focus but it's very clean. And simple and colors are good
Updates

Please rebook brief. I have added some important detail. Thanks

Relook brief. I have added,important detail. Thanks

Target Market(s)

Corporate buyers
This is not for retail selling to consumers
Price it's viewed only after secure login

Industry/Entity Type

Shopping

Colors
acd037
cadf82
fbc995
fce7d3
faa54b

Requirements
Must have
• Luxury. Think luxury. Very high end yet modern like the catalogue
Use banners on home page
Should not have
• Don't use the blue as the main color. It's too cheap.
No products on home page

```html
<!DOCTYPE html>
<html lang="en">
<head>
<meta charset="utf-8">
<title>The Harwell Selection</title>
<link rel="stylesheet" href="https://fonts.googleapis.com/css2?family=Cabin:wght@400;600;700&family=Questrial&display=swap">
<style>
:root{
  --brand:#acd037;
  --brand-deep:#6e8a1a;
  --brand-soft:#cadf82;
  --accent:#faa54b;
  --peach:#fbc995;
  --cream:#fce7d3;
  --ink:#333;
  --dark-btn:#3a3a3a;
  --rule:#d8cbbd;
  --white:#fff;
}
*{box-sizing:border-box;margin:0;padding:0}
html,body{width:732px;height:1200px;overflow:hidden;background:var(--white)}
body{position:relative;font-family:'Cabin',sans-serif;color:var(--ink)}
.abs{position:absolute}

.top-bar{left:0;top:0;width:732px;height:26px;background:var(--brand-deep);color:var(--white);font-size:8px;font-weight:700}
.top-bar .links{position:absolute;left:12px;top:8px;display:flex;gap:14px;align-items:center}
.top-bar .links span{display:flex;align-items:center;gap:3px}
.top-bar .info{position:absolute;right:12px;top:8px}

.site-name{left:16px;top:40px;font-family:'Questrial',sans-serif;font-size:27px;color:var(--brand-deep)}
.category-select{left:351px;top:50px;width:89px;height:17px;border:1px solid #bbb;font-size:7px;color:#666;padding:4px 5px}
.category-select svg{position:absolute;right:5px;top:5px}
.search-btn{left:443px;top:50px;width:45px;height:17px;background:var(--brand-deep);color:var(--white);font-size:7px;font-weight:700;text-align:center;line-height:17px}
.search-field{left:494px;top:49px;width:164px;height:18px;border:1px solid #bbb;font-size:7px;color:#777;padding:4px 6px}
.search-field svg{position:absolute;right:5px;top:3px}
.social-square{width:20px;height:20px;background:var(--brand);border-radius:3px;top:47px}
.header-rule{left:0;top:85px;width:732px;height:1px;background:var(--brand)}

.side-nav{left:45px;top:111px;width:132px;list-style:none}
.side-nav li{height:28.5px;line-height:26px;padding-left:6px;font-size:11px;color:#555}
.side-nav li.active{background:var(--brand-soft);color:var(--white);clip-path:polygon(0 0,88% 0,100% 50%,88% 100%,0 100%);width:132px}
.call-box{left:45px;top:341px;width:132px;height:95px;background:linear-gradient(#fff,var(--cream));text-align:center}
.call-icon{position:absolute;left:48px;top:8px;width:36px;height:30px;border-radius:50%;background:radial-gradient(circle,var(--peach),var(--accent))}
.call-box .label{position:absolute;left:0;right:0;top:52px;font-family:'Questrial',sans-serif;font-size:14px;color:#222}
.call-box .number{position:absolute;left:0;right:0;top:69px;font-family:'Questrial',sans-serif;font-size:16px;color:#222}

.hero{left:194px;top:104px;width:493px;height:332px;background:linear-gradient(90deg,#f4f2ee 0%,#ece8e1 55%,#e2d9c8 75%,#d6ccba 100%)}
.hero-title{left:236px;top:182px;width:210px;font-family:'Questrial',sans-serif;font-size:30px;line-height:35px;color:#2a2a2a}
.hero-shop{left:239px;top:335px;width:74px;height:25px;background:var(--brand-deep);color:var(--white);font-size:9px;font-weight:700;text-align:center;line-height:25px}
.hero-seal{left:609px;top:360px;width:60px;height:60px;border-radius:50%;background:#9a9182;opacity:.5}

.mood-banner{top:451px;height:179px;width:203px}
.mood-title{top:637px;width:203px;text-align:center;font-size:16px;letter-spacing:.5px;color:#444}
.mood-rule{top:660px;width:203px;height:1px;background:var(--rule)}
.mood-text{top:671px;width:203px;text-align:center;font-size:7.2px;line-height:8.9px;color:#555}
.btn{height:20px;width:63px;color:var(--white);font-size:8px;font-weight:700;text-align:center;line-height:20px;top:734px}
.btn-details{background:var(--accent)}

.about-panel{left:45px;top:774px;width:642px;height:120px;background:var(--cream);text-align:center}
.about-panel h2{margin-top:19px;font-weight:400;font-size:19px;color:#333}
.about-panel p{margin:5px auto 0;width:570px;font-size:10.4px;line-height:13px;color:#333}

.newsletter-title{left:0;width:732px;top:908px;text-align:center;font-family:'Questrial',sans-serif;font-size:20px;color:#111}
.newsletter-form{left:178px;top:944px;width:383px;height:24px;border:1px solid #bbb}
.newsletter-form .field{position:absolute;left:6px;top:6px;font-size:9.5px;color:#999}
.newsletter-form .submit{position:absolute;right:2px;top:2px;width:63px;height:18px;background:var(--dark-btn);color:var(--white);font-size:8px;font-weight:700;text-align:center;line-height:18px}
.section-rule{left:45px;top:981px;width:642px;height:1px;background:var(--rule)}

.partner{top:1005px;font-size:9px;color:#777;text-align:center;width:90px}
.fine-print{left:185px;top:1044px;width:400px;text-align:center;font-size:5.6px;line-height:8px;color:#666}

.site-footer{left:0;top:1085px;width:732px;height:115px;background:var(--brand-deep);color:var(--white);text-align:center;font-size:7.8px}
.footer-links{margin-top:12px;display:flex;justify-content:center;gap:3px}
.footer-links span,.footer-email{text-decoration:underline}
.footer-address{margin-top:5px;line-height:11px}
.footer-icons{margin-top:7px;display:flex;justify-content:center;gap:5px}
.footer-icons .sq{width:14px;height:14px;background:var(--cream);border-radius:2px}
.copyright{margin-top:8px}
</style>
</head>
<body>

<header>
  <div class="abs top-bar">
    <div class="links">
      <span>Login</span>
      <span>Contact</span>
      <span><svg width="9" height="8" viewBox="0 0 10 9"><path d="M5 8.5 1 4.5A2.3 2.3 0 0 1 5 1.6 2.3 2.3 0 0 1 9 4.5Z" fill="none" stroke="#fff" stroke-width="1.2"/></svg>Wishlist</span>
      <span>My Cart (0)</span>
    </div>
    <div class="info">For Australia &amp; South East Asia Larkmoor Grand Email for information PH: +61 400 555 019</div>
  </div>

  <div class="abs site-name">The Harwell Selection</div>
  <div class="abs category-select">Select...<svg width="7" height="6" viewBox="0 0 7 6"><path d="M0 0h7L3.5 6z" fill="#333"/></svg></div>
  <div class="abs search-btn">SEARCH</div>
  <div class="abs search-field">Search by products<svg width="11" height="11" viewBox="0 0 11 11"><circle cx="4.5" cy="4.5" r="3.3" fill="none" stroke="#333" stroke-width="1.2"/><path d="M7 7l3 3" stroke="#333" stroke-width="1.5"/></svg></div>
  <div class="abs social-square" style="left:668px"></div>
  <div class="abs social-square" style="left:694px"></div>
  <div class="abs header-rule"></div>
</header>

<nav>
  <ul class="abs side-nav">
    <li>Bath Towels</li>
    <li class="active">Robes</li>
    <li>Accessories</li>
    <li>Mats</li>
    <li>Pool &amp; Beach</li>
    <li>Blankets &amp; Throws</li>
    <li>Massage &amp; Sauna</li>
    <li>New Collection</li>
  </ul>
  <div class="abs call-box">
    <div class="call-icon" role="img" aria-label="Customer service icon"></div>
    <div class="label">Call to Order</div>
    <div class="number">1.800.555.0142</div>
  </div>
</nav>

<main>
  <section>
    <div class="abs hero" role="img" aria-label="Cream waffle bath robe on a dress form in a bright room"></div>
    <h1 class="abs hero-title" style="font-weight:400">The Harwell Selection A Distributor of Fine Linen</h1>
    <div class="abs hero-shop">SHOP NOW</div>
    <div class="abs hero-seal" role="img" aria-label="Quality seal"></div>
  </section>

  <section>
    <div class="abs mood-banner" style="left:45px;background:linear-gradient(135deg,#c9b79c,#ece4d8 45%,#faf7f2)" role="img" aria-label="Mood banner: guest relaxing poolside in a white cotton robe"></div>
    <div class="abs mood-banner" style="left:265px;background:linear-gradient(160deg,#8fa43a 0%,#b7c66c 35%,#c9a882 65%,#8a7660 100%)" role="img" aria-label="Texture close-up: layered woven throws"></div>
    <div class="abs mood-banner" style="left:484px;background:linear-gradient(180deg,#fbf9f6 0%,#ebe5dc 65%,#4a4238 100%)" role="img" aria-label="Texture close-up: folded white waffle towels"></div>

    <h3 class="abs mood-title" style="left:45px;font-weight:400">ROBES</h3>
    <h3 class="abs mood-title" style="left:265px;font-weight:400">THROWS</h3>
    <h3 class="abs mood-title" style="left:484px;font-weight:400">TOWELS</h3>
    <div class="abs mood-rule" style="left:45px"></div>
    <div class="abs mood-rule" style="left:265px"></div>
    <div class="abs mood-rule" style="left:484px"></div>

    <p class="abs mood-text" style="left:45px">For a daily retreat from modern living, treat your skin to pure cotton loungewear. Here you will find a distinctive collection of bath robes with contemporary patterns and styling. For premium bath and spa comfort, chose from our array of absorbent, yet lightweight cotton bath robes.</p>
    <p class="abs mood-text" style="left:265px">There is nothing so inviting as a luxurious blanket or decorative throw. The Harwell Selection brings you an assortment of warm throws in several colors to accent your home décor. Our blankets and throws are quality pieces, crafted from the finest cotton, mohair, or baby alpaca.</p>
    <p class="abs mood-text" style="left:484px">Take a moment to relax every day with The Harwell Selection's spa-quality bath towels. Here you will find a collection of premium lightweight bath towels that are woven with the finest cotton for a truly luxurious bath and spa experience. Browse our collections to find a towel set to suit your tastes.</p>

    <div class="abs btn btn-details" style="left:115px">DETAILS</div>
    <div class="abs btn btn-details" style="left:335px">DETAILS</div>
    <div class="abs btn btn-details" style="left:554px">DETAILS</div>
  </section>

  <section class="abs about-panel">
    <h2>Wrap Yourself in Luxury...</h2>
    <p>Here at The Harwell Selection we deliver the finest in cotton towels, loungewear, and bath accessories to ensure that your bath and spa collection not only looks great, but also offers supreme comfort, absorbency, and durability. By combining quality, lightweight fibers and luxurious weaves, The Harwell Selection allows you to transform your bathroom, spa, or poolside into a true retreat.</p>
  </section>

  <section>
    <h2 class="abs newsletter-title" style="font-weight:400">Newsletter Signup</h2>
    <div class="abs newsletter-form">
      <span class="field">Email Address...</span>
      <span class="submit">SIGN UP</span>
    </div>
    <div class="abs section-rule"></div>
  </section>

  <section>
    <div class="abs partner" style="left:186px">The Calder House</div>
    <div class="abs partner" style="left:276px">Oakhaven Suites</div>
    <div class="abs partner" style="left:372px">Marisol Bay</div>
    <div class="abs partner" style="left:476px">The Ashby Lodge</div>
    <p class="abs fine-print">*Receive one free matching robe with your valid purchase of one robe on our online store. Free robe will match in style and size. Offer valid from February 4 through February 13 at midnight EST. Offer may be revoked and may not be redeemed for a later purchase if the order is cancelled or refunded. Offer may end at any time. Not valid on third-party sites.</p>
  </section>
</main>

<footer class="abs site-footer">
  <div class="footer-links"><span>About Us</span> <span>Customer Service</span> <span>Wholesalers</span> <span>Contact Us</span> <span>Email Registration</span></div>
  <div class="footer-address">
    48 Linden Row, Port Avalon, FL 30999<br>
    Phone: (305) 555-0120, Fax: (305) 555-0188, Toll Free: (877) 6 HARWELL or (800) 555-0142<br>
    <span class="footer-email">contact@harwellselection.example</span>
  </div>
  <div class="footer-icons">
    <svg width="16" height="14" viewBox="0 0 16 14"><rect x="0.5" y="1.5" width="15" height="11" rx="1.5" fill="#fce7d3"/><path d="M1 2.5l7 5 7-5" fill="none" stroke="#6e8a1a" stroke-width="1.2"/></svg>
    <div class="sq"></div>
    <div class="sq"></div>
  </div>
  <div class="copyright">Copyright ©2014, The Harwell Selection, All rights reserved</div>
</footer>

</body>
</html>
```